Business Card Design - Commercial Photographer

Professional Photographer requires eye catching creative business card. The design will need to incorporate my current logo in some form & not clash with my website tones & colours ( although website will be re designed in the future ). I'm currently shooting new folios in Commercial, Fashion & Architecture so I'm marketing to professional clients rather than portrait / wedding clients. Looking for something professional & creative.

Industry/Entity Type

Marketing

Requirements
Must have
• Website address - www.brightmarrowlens.com.au

Phone number - 0452786104

Email - info@brightmarrowlens.com.au

```html
<!DOCTYPE html>
<html lang="en">
<head>
<meta charset="utf-8">
<title>Bright Marrow Lens – Business Card</title>
<link href="https://fonts.googleapis.com/css2?family=Roboto+Condensed:wght@300;700&display=swap" rel="stylesheet">
<style>
  :root {
    --page: #ffffff;
    --card-dark: #2b2725;
    --ink-light: #f2efec;
    --photo-deep: #2e2a26;
    --photo-mid: #5a4f45;
    --photo-warm: #8a7260;
    --lens-glow: #b7977c;
  }
  html, body {
    margin: 0;
    width: 1200px;
    height: 1000px;
    overflow: hidden;
    background: var(--page);
  }
  .canvas {
    position: relative;
    width: 1200px;
    height: 1000px;
  }
  .card {
    position: absolute;
    left: 328px;
    width: 537px;
    height: 328px;
    overflow: hidden;
  }
  .card--front { top: 163px; }
  .card--back { top: 521px; background: var(--card-dark); }

  .front-photo {
    position: absolute;
    inset: 0;
    background:
      radial-gradient(circle at 50% 50%, var(--lens-glow) 0%, var(--photo-warm) 30%, var(--photo-mid) 58%, var(--photo-deep) 100%);
  }
  .lens-rings {
    position: absolute;
    inset: 0;
  }
  .brand-name {
    font-family: "Roboto Condensed", "Arial Narrow", sans-serif;
    font-weight: 700;
    color: var(--ink-light);
    text-transform: uppercase;
    line-height: 0.92;
    letter-spacing: 0.5px;
    margin: 0;
  }
  .card--front .brand-name {
    position: absolute;
    left: 0;
    right: 0;
    top: 110px;
    text-align: center;
    font-size: 44px;
  }
  .card--back .brand-name {
    position: absolute;
    left: 64px;
    top: 52px;
    font-size: 40px;
  }
  .contact {
    position: absolute;
    left: 278px;
    top: 200px;
    margin: 0;
    padding: 0;
    list-style: none;
    font-family: "Roboto Condensed", "Arial Narrow", sans-serif;
    color: var(--ink-light);
  }
  .contact li {
    font-size: 18px;
    font-weight: 300;
    height: 30px;
    line-height: 30px;
    letter-spacing: 0.2px;
  }
  .contact .contact-phone {
    font-weight: 700;
    letter-spacing: 1px;
  }
</style>
</head>
<body>
<main class="canvas">
  <section class="card card--front">
    <div class="front-photo" role="img" aria-label="Sepia period photograph of a vintage motor garage with a man beside an old car and a mother holding children, seen through a lens-like circular focus"></div>
    <svg class="lens-rings" width="537" height="328" viewBox="0 0 537 328" aria-hidden="true">
      <circle cx="268" cy="164" r="220" fill="none" stroke="rgba(255,255,255,0.12)" stroke-width="1"/>
      <circle cx="268" cy="164" r="125" fill="rgba(40,32,28,0.18)" stroke="rgba(255,255,255,0.1)" stroke-width="1"/>
    </svg>
    <p class="brand-name">Bright<br>Marrow<br>Lens</p>
  </section>

  <section class="card card--back">
    <p class="brand-name">Bright<br>Marrow<br>Lens</p>
    <ul class="contact">
      <li class="contact-web">www.brightmarrowlens.com.au</li>
      <li class="contact-phone">0452 786 104</li>
      <li class="contact-email">info@brightmarrowlens.com.au</li>
    </ul>
  </section>
</main>
</body>
</html>
```